Stationary Package
Business Card / Letterhead / Envelop
I need double sided standard sized Business Card [3.5" x 2"]
use same look and feel font(s)
Professional
Daniel Whitfield
Marketing Strategist
4518 Harwick Crescent
Mississauga, Ontario, L4T 3K8
danielwhitfield@vellorahaus.com
www.vellorahaus.com
design package for the marketing industry
Logo with tag line
plus the website address
Logo and Tag Line
eps logo
pdf logo version

```html
<!DOCTYPE html>
<html lang="en">
<head>
<meta charset="utf-8">
<title>Daniel Whitfield – Business Cards</title>
<link rel="stylesheet" href="https://fonts.googleapis.com/css2?family=Jost:wght@400;500;700&display=swap">
<style>
  :root {
    --page-bg: #ffffff;
    --brand-blue: #1f6fd1;
    --brand-blue-deep: #1a3fae;
    --blue-light: #4aa0ec;
    --blue-dark: #1d2fb0;
    --swoosh-grey: #6d6f75;
    --charcoal-light: #5a5a5c;
    --charcoal-dark: #2f2f31;
    --white: #ffffff;
    --card-edge: #c9ccd3;
  }
  * { margin: 0; padding: 0; box-sizing: border-box; }
  html, body {
    width: 1200px; height: 713px; overflow: hidden;
    background: var(--page-bg);
    font-family: "Jost", "Futura", sans-serif;
  }
  .canvas { position: relative; width: 1200px; height: 713px; }
  .card {
    position: absolute; overflow: hidden;
    border: 1px solid var(--card-edge);
  }
  .card--front { left: 29px; top: 29px; width: 571px; height: 324px; background: var(--white); }
  .card--back-blue {
    left: 614px; top: 29px; width: 557px; height: 324px;
    background: radial-gradient(ellipse at 45% 40%, #2f63e0 0%, var(--brand-blue-deep) 55%, #1a2a9a 100%);
  }
  .card--back-grey {
    left: 329px; top: 365px; width: 547px; height: 331px;
    background: radial-gradient(ellipse at 50% 35%, var(--charcoal-light) 0%, #444446 50%, var(--charcoal-dark) 100%);
  }
  .card__wave { position: absolute; left: 0; top: 0; width: 100%; height: 100%; }

  .brand {
    position: absolute; left: 0; width: 100%;
    display: flex; flex-direction: column; align-items: center;
  }
  .brand__dot { width: 26px; height: 26px; border-radius: 50%; margin-bottom: 10px; }
  .brand__name { font-weight: 700; font-size: 26px; letter-spacing: 0.5px; line-height: 1; }
  .brand__tagline { font-weight: 400; font-size: 13px; margin-top: 4px; line-height: 1; }

  .card--front .brand { top: 48px; }
  .card--front .brand__dot { background: var(--brand-blue); }
  .card--front .brand__name { color: var(--brand-blue); }
  .card--front .brand__tagline { color: var(--brand-blue); }

  .card--back-blue .brand { top: 100px; }
  .card--back-grey .brand { top: 106px; }
  .card--back-blue .brand__dot, .card--back-grey .brand__dot { background: var(--white); }
  .card--back-blue .brand__name, .card--back-blue .brand__tagline,
  .card--back-grey .brand__name, .card--back-grey .brand__tagline { color: var(--white); }

  .contact {
    position: absolute; left: 24px; top: 220px;
    color: var(--white); font-size: 12.5px; line-height: 16px;
  }
  .contact__label { font-weight: 700; }
  .holder {
    position: absolute; right: 30px; top: 220px; text-align: right;
    color: var(--white); line-height: 18px;
  }
  .holder__name { font-weight: 700; font-size: 15px; }
  .holder__role { font-size: 12.5px; }

  .website {
    position: absolute; left: 0; width: 100%; text-align: center;
    color: var(--white); font-size: 12.5px;
  }
  .card--back-blue .website { top: 250px; }
  .card--back-grey .website { top: 252px; }
</style>
</head>
<body>
<div class="canvas">

  <section class="card card--front">
    <svg class="card__wave" viewBox="0 0 571 324" preserveAspectRatio="none" aria-hidden="true">
      <defs>
        <linearGradient id="front-blue" x1="0" y1="0" x2="0" y2="1">
          <stop offset="0" stop-color="#3b8fe6"/>
          <stop offset="1" stop-color="#1d48c0"/>
        </linearGradient>
      </defs>
      <path d="M0 150 Q285 240 571 150 L571 324 L0 324 Z" fill="url(#front-blue)"/>
      <path d="M0 138 Q285 238 571 138 L571 150 Q285 246 0 150 Z" fill="#6d6f75" opacity="0.85"/>
    </svg>
    <div class="brand">
      <span class="brand__dot"></span>
      <span class="brand__name">DANIEL WHITFIELD</span>
      <span class="brand__tagline">Vellora Haus</span>
    </div>
    <address class="contact" style="font-style:normal">
      4518 Harwick Crescent Mississauga,<br>
      Ontario, L4T 3K8<br>
      <span class="contact__label">C :</span> 416 555 0187<br>
      <span class="contact__label">E :</span> danielwhitfield@vellorahaus.com<br>
      www.vellorahaus.com
    </address>
    <div class="holder">
      <div class="holder__name">Daniel Whitfield</div>
      <div class="holder__role">Marketing Strategist</div>
    </div>
  </section>

  <section class="card card--back-blue">
    <div class="brand">
      <span class="brand__dot"></span>
      <span class="brand__name">DANIEL WHITFIELD</span>
      <span class="brand__tagline">Vellora Haus</span>
    </div>
    <div class="website">www.vellorahaus.com</div>
  </section>

  <section class="card card--back-grey">
    <div class="brand">
      <span class="brand__dot"></span>
      <span class="brand__name">DANIEL WHITFIELD</span>
      <span class="brand__tagline">Vellora Haus</span>
    </div>
    <div class="website">www.vellorahaus.com</div>
  </section>

</div>
</body>
</html>
```